A design led business card for the construction industry

High-end business card to match logo. White logo on dark grey/off black to the front. Matching dark font on white to back, possibly with logo design again.

We offer construction and project management services to commercial and private clients in the UK. Projetcs range from newbuilds, conversion of listed buildings and refurbishments and extensions of existing homes. Our focus is on quality and attention to detail using the highest skills.

Contact Information for Business Card

Name; Dorian Hatch BSc
Position; Project Manager
Mobile; 07962 804 157
Tel; 01632 958412
email; dorian@framelark.co.uk
web; www.framelark.co.uk
Address; Henley on Thames, KT4 7PZ

Colors

Designer to choose only greyscale colors for use in the design.

Requirements
Must have
• To include the below description of the business,

CONSTRUCTION - PROJECT MANAGEMENT
Nice to have
• The posibility of the top back of the card being used as a ruler. So will have a measurement to scale in mm or an architect scale of 1:50
Should not have
• Should not be portrait

```html
<!DOCTYPE html>
<html lang="en">
<head>
<meta charset="utf-8">
<title>Framelark Business Card</title>
<link href="https://fonts.googleapis.com/css2?family=Poppins:wght@300;400;600&display=swap" rel="stylesheet">
<style>
  :root {
    --stage: #1c1c1c;
    --card-front: #232323;
    --pattern: #2b2b2b;
    --card-back: #ffffff;
    --ink-light: #ffffff;
    --ink-dark: #1f1f1f;
    --ink-dark-soft: #555555;
  }
  * { margin: 0; padding: 0; box-sizing: border-box; }
  html, body {
    width: 1200px; height: 1200px; overflow: hidden;
    background: var(--stage);
    font-family: "Poppins", sans-serif;
  }
  .stage { position: relative; width: 1200px; height: 1200px; }
  .card {
    position: absolute; left: 120px; width: 960px; height: 540px;
    border-radius: 26px; overflow: hidden;
  }
  .card--front { top: 40px; background: var(--card-front); color: var(--ink-light); }
  .card--back { top: 620px; background: var(--card-back); color: var(--ink-dark); }

  .card__pattern {
    position: absolute; inset: 0;
    background: linear-gradient(135deg, var(--pattern), var(--card-front));
  }

  .brand {
    position: absolute; display: flex; align-items: center; gap: 22px;
    font-weight: 300; letter-spacing: 0.32em; white-space: nowrap;
  }
  .brand__square { border: 4px solid currentColor; flex: none; }
  .card--front .brand {
    left: 50%; top: 50%; transform: translate(-50%, -50%);
    font-size: 40px;
  }
  .card--front .brand__square { width: 48px; height: 48px; }

  .person { position: absolute; left: 80px; top: 60px; }
  .person__name { font-size: 36px; font-weight: 600; line-height: 1.2; }
  .person__role { font-size: 22px; font-weight: 300; color: var(--ink-dark-soft); margin-top: 2px; }
  .person__rule { width: 20px; height: 3px; background: var(--ink-dark); margin-top: 14px; }

  .contacts { position: absolute; left: 80px; bottom: 60px; list-style: none; }
  .contacts li {
    display: flex; align-items: center; gap: 14px;
    font-size: 23px; font-weight: 300; line-height: 1.5;
  }
  .contacts svg { width: 22px; height: 22px; flex: none; }

  .back-brand { position: absolute; right: 70px; top: 290px; text-align: right; }
  .back-brand .brand { position: static; font-size: 38px; justify-content: flex-end; }
  .back-brand .brand__square { width: 44px; height: 44px; }
  .services {
    margin-top: 18px; font-size: 15px; font-weight: 400;
    letter-spacing: 0.14em; color: var(--ink-dark-soft); white-space: nowrap;
  }
</style>
</head>
<body>
<main class="stage">
  <section class="card card--front">
    <div class="card__pattern" role="img" aria-label="Faint repeating brand pattern across the card"></div>
    <div class="brand"><span class="brand__square"></span>FRAMELARK</div>
  </section>

  <section class="card card--back">
    <div class="person">
      <h1 class="person__name">Dorian Hatch BSc</h1>
      <p class="person__role">Project Manager</p>
      <div class="person__rule"></div>
    </div>

    <ul class="contacts">
      <li>
        <svg viewBox="0 0 24 24" fill="none" stroke="#1f1f1f" stroke-width="2"><rect x="6" y="2" width="12" height="20" rx="2"/><line x1="11" y1="18" x2="13" y2="18"/></svg>
        07962 804 157
      </li>
      <li>
        <svg viewBox="0 0 24 24" fill="#1f1f1f"><path d="M6.6 10.8a15 15 0 0 0 6.6 6.6l2.2-2.2c.3-.3.7-.4 1-.2 1.1.4 2.3.6 3.6.6.6 0 1 .4 1 1V20c0 .6-.4 1-1 1A17 17 0 0 1 3 4c0-.6.4-1 1-1h3.5c.6 0 1 .4 1 1 0 1.3.2 2.5.6 3.6.1.3 0 .7-.2 1z"/></svg>
        01632 958412
      </li>
      <li>
        <svg viewBox="0 0 24 24" fill="#1f1f1f"><path d="M2 5h20v14H2z"/><path d="M2 5l10 8 10-8" fill="none" stroke="#ffffff" stroke-width="1.8"/></svg>
        dorian@framelark.co.uk
      </li>
      <li>
        <svg viewBox="0 0 24 24" fill="none" stroke="#1f1f1f" stroke-width="1.8"><circle cx="12" cy="12" r="10"/><ellipse cx="12" cy="12" rx="4.5" ry="10"/><line x1="2" y1="12" x2="22" y2="12"/><line x1="4" y1="7" x2="20" y2="7"/><line x1="4" y1="17" x2="20" y2="17"/></svg>
        www.framelark.co.uk
      </li>
      <li>
        <svg viewBox="0 0 24 24" fill="#1f1f1f"><path d="M12 2a7 7 0 0 0-7 7c0 5 7 13 7 13s7-8 7-13a7 7 0 0 0-7-7zm0 9.5A2.5 2.5 0 1 1 12 6.5a2.5 2.5 0 0 1 0 5z"/></svg>
        Henley on Thames, KT4 7PZ
      </li>
    </ul>

    <div class="back-brand">
      <div class="brand"><span class="brand__square"></span>FRAMELARK</div>
      <p class="services">CONSTRUCTION - PROJECT MANAGEMENT</p>
    </div>
  </section>
</main>
</body>
</html>
```